High End Mechanic Business Card Design Project

Automotive Business - Repair, service and sales
Bold background with clarity of text

Industry/Entity Type

Automotive

Contact Information for Business Card

Black background with silver or white kvt 418 lorne coupe at the bottom right angered with the business name and address at the top left.. Also to include a compass near the business name and the text... Sales Service RepairAdded photos as EXAMPLES. Don't want the actual n, s, e w on the compass picture but to know that it is a compass.

Font styles to use
Sans Serif

Requirements
Must have
• Creativity, black background, Images: 4 Lorne KVT Coupe & Compass (without text)

```html
<!DOCTYPE html>
<html lang="en">
<head>
<meta charset="utf-8">
<title>Harrow Ridge Motors – Business Card</title>
<link rel="stylesheet" href="https://fonts.googleapis.com/css2?family=Roboto+Slab:wght@300;400&display=swap">
<style>
  :root {
    --page-bg: #e9e6e2;
    --card-black: #0c0d0f;
    --card-dark: #1b1d21;
    --brand-blue: #2f86b8;
    --banner-blue: #1f78b0;
    --banner-light: #3a9bd3;
    --address-grey: #d2d4d6;
    --mark-grey: #3a3c40;
    --car-white: #e8eaec;
    --car-shadow: #8e949a;
  }
  * { box-sizing: border-box; margin: 0; padding: 0; }
  html, body { width: 1200px; height: 800px; overflow: hidden; }
  body {
    background: var(--page-bg);
    position: relative;
    font-family: "Roboto Slab", serif;
  }
  .card {
    position: absolute;
    width: 472px;
    height: 269px;
    overflow: hidden;
    background: radial-gradient(ellipse at 50% 40%, var(--card-dark) 0%, var(--card-black) 75%);
    box-shadow: 0 6px 14px rgba(0,0,0,0.35);
  }
  .card--front { left: 112px; top: 198px; }
  .card--back { left: 622px; top: 334px; }

  .business-name {
    position: absolute;
    left: 0; right: 0;
    text-align: center;
    font-weight: 400;
    font-size: 36px;
    line-height: 1;
    color: var(--brand-blue);
    white-space: nowrap;
  }
  .card--front .business-name { top: 26px; padding-left: 2px; }
  .card--back .business-name { top: 176px; }

  .brand-dot {
    position: absolute;
    border-radius: 50%;
    background: var(--mark-grey);
  }
  .card--front .brand-dot { left: 31px; top: 87px; width: 80px; height: 80px; }
  .card--back .brand-dot { left: 196px; top: 57px; width: 84px; height: 84px; }

  .address {
    position: absolute;
    left: 120px;
    width: 246px;
    top: 85px;
    text-align: center;
    font-weight: 300;
    font-size: 18px;
    line-height: 29px;
    color: var(--address-grey);
    font-style: normal;
  }

  .services-banner {
    position: absolute;
    left: 0;
    top: 209px;
    width: 251px;
    height: 30px;
    padding-left: 12px;
    background: linear-gradient(180deg, var(--banner-light), var(--banner-blue));
    clip-path: polygon(0 0, 100% 0, 94% 100%, 0 100%);
    color: #ffffff;
    font-weight: 400;
    font-size: 18px;
    line-height: 30px;
    white-space: nowrap;
  }

  .car-photo {
    position: absolute;
    left: 273px;
    top: 170px;
    width: 190px;
    height: 88px;
    border-radius: 40% 45% 18% 18% / 55% 55% 22% 22%;
    background: linear-gradient(180deg, var(--car-white) 0%, var(--car-white) 60%, var(--car-shadow) 100%);
  }
</style>
</head>
<body>
  <section class="card card--front" aria-label="Business card front">
    <h1 class="business-name">Harrow Ridge Motors</h1>
    <span class="brand-dot" aria-hidden="true"></span>
    <address class="address">
      2280 Linden Ridge Pkwy,<br>
      Dalton, GA 30720<br>
      Tel. 555.207.4416
    </address>
    <div class="services-banner">Sales - Service - Repair</div>
    <div class="car-photo" role="img" aria-label="White KVT 4 Lorne coupe, front three-quarter view"></div>
  </section>

  <section class="card card--back" aria-label="Business card back">
    <span class="brand-dot" aria-hidden="true"></span>
    <h2 class="business-name">Harrow Ridge Motors</h2>
  </section>
</body>
</html>
```